Label Redesign For Hemp Oil Tincture Bottle*

I need a label redesigned for Marbleleaf Hemp, current bottle label and logo is attached. The current label doesn't standout, not sure if its the font size or colors on the existing label. It is very important to have on the label that this is a Premium Full Spectrum Hemp Oil that is 2000mg. Then after the label is redesigned and approved, I would need to packaging to be designed to match the approved label design.
This Hemp oil has a relaxing effect to help ease mental and emotional stress, tension and worry. The Omega Fatty Acids it contains also naturally improves your mood and overall brain function, causing you to feel more alert and focused. Hemp Oil helps with insomnia. Take some 2-3 hours before bedtime, you will feel relaxed yet aware of how tired you are that it will lead to a good night's sleep. Hemp Oil helps ease chronic pain and inflammation from conditions such as arthritis, fibromyalgia, lupus, and MS. As a pain relief supplement, it is a safer, natural, non-chemical and non-addictive alternative to prescription painkillers.

Target Market(s)

Adults

Industry/Entity Type

Supplement

Font styles to use
Serif
Sans Serif

Colors

Designer to choose colors to be used in the design.

Requirements
Must have
• All information thats on current label but where it says 750 in the front of the existing label, it needs to say 2000. The 2000 should be prominent on the label.

```html
<!DOCTYPE html>
<html lang="en">
<head>
<meta charset="utf-8">
<title>Marbleleaf Hemp – Premium Full Spectrum Hemp Oil Label</title>
<link rel="stylesheet" href="https://fonts.googleapis.com/css2?family=Jost:wght@300;400&display=swap">
<style>
  :root {
    --backdrop: #eceef0;
    --label: #ffffff;
    --label-shade: #ececec;
    --ink: #2b2b2b;
    --rule: #333333;
    --accent-green: #c8cc5e;
    --drop-light: #e6e36a;
    --drop-dark: #b0ab1c;
    --badge-ring: #3a3a3a;
    --badge-fill: #eaf0d8;
  }
  * { margin: 0; padding: 0; box-sizing: border-box; }
  html, body {
    width: 1029px; height: 1200px; overflow: hidden;
    background: var(--backdrop);
  }
  .canvas { position: relative; width: 1029px; height: 1200px; }
  .label {
    position: absolute; left: 124px; top: 66px;
    width: 780px; height: 1068px;
    background: linear-gradient(90deg, var(--label-shade) 0%, var(--label) 18%, var(--label) 82%, var(--label-shade) 100%);
    font-family: "Jost", sans-serif;
    color: var(--ink);
  }
  .brand {
    position: absolute; left: 0; right: 0; top: 110px;
    display: flex; align-items: center; justify-content: center; gap: 22px;
  }
  .brand-dot { width: 58px; height: 58px; border-radius: 50%; background: var(--accent-green); }
  .brand-name { font-size: 50px; font-weight: 400; color: var(--ink); letter-spacing: 1px; }
  .rule {
    position: absolute; left: 70px; right: 70px; height: 3px; background: var(--rule);
  }
  .rule-top { top: 250px; }
  .rule-bottom { top: 423px; }
  .grade {
    position: absolute; left: 0; right: 0; top: 282px;
    text-align: center; font-weight: 300; font-size: 54px; line-height: 60px;
  }
  .strength {
    position: absolute; left: 0; right: 0; top: 458px;
    text-align: center; font-weight: 400; font-size: 60px;
  }
  .product {
    position: absolute; left: 0; right: 0; top: 560px;
    text-align: center; font-weight: 400; font-size: 112px; letter-spacing: 3px;
  }
  .drop { position: absolute; left: 335px; top: 710px; width: 110px; height: 180px; }
  .badge { position: absolute; left: 552px; top: 722px; width: 192px; height: 192px; }
  .band {
    position: absolute; left: 0; right: 0; top: 908px; height: 42px;
    background: var(--accent-green);
  }
</style>
</head>
<body>
  <main class="canvas">
    <section class="label">
      <div class="brand">
        <span class="brand-dot"></span>
        <span class="brand-name">Marbleleaf Hemp</span>
      </div>
      <div class="rule rule-top"></div>
      <p class="grade">PREMIUM<br>FULL SPECTRUM</p>
      <div class="rule rule-bottom"></div>
      <p class="strength">2000MG</p>
      <h1 class="product">HEMP OIL</h1>
      <svg class="drop" viewBox="0 0 110 180" aria-hidden="true">
        <defs>
          <linearGradient id="oil" x1="0" y1="0" x2="1" y2="1">
            <stop offset="0" stop-color="var(--drop-light)"/>
            <stop offset="1" stop-color="var(--drop-dark)"/>
          </linearGradient>
        </defs>
        <path d="M55 0 C62 45 108 90 108 125 A53 53 0 0 1 2 125 C2 90 48 45 55 0 Z" fill="url(#oil)"/>
      </svg>
      <svg class="badge" viewBox="0 0 192 192" aria-hidden="true">
        <circle cx="96" cy="96" r="92" fill="var(--label)"/>
        <circle cx="96" cy="96" r="60" fill="var(--badge-fill)" stroke="var(--badge-ring)" stroke-width="5"/>
      </svg>
      <div class="band"></div>
    </section>
  </main>
</body>
</html>
```